Open sky balance Business cards - yoga studio

We need business cards for our yoga studio Openbreath Harmony.
We would like to see designs that include the colour blue and our logo.
The business card should communicate a feeling of strength and calm

Business

Requirements
Must have
• The business card must include
"Maren Tollefsen - Director"
and
"42 Quillfern Avenue
Dunmorrow
VIC 3806
Ph - 0451 628 904"

```html
<!DOCTYPE html>
<html lang="en">
<head>
<meta charset="UTF-8">
<title>Openbreath Harmony – Business Cards</title>
<link rel="stylesheet" href="https://fonts.googleapis.com/css2?family=Open+Sans:wght@300;400;700&display=swap">
<style>
  :root {
    --backdrop: #ebe8e5;
    --card-white: #fbfbfb;
    --brand-teal: #5aabbc;
    --logo-teal: #4fa6b3;
    --ink-dark: #17272b;
    --ink-light: #ffffff;
  }
  * { box-sizing: border-box; margin: 0; padding: 0; }
  html, body {
    width: 1200px;
    height: 997px;
    overflow: hidden;
    background: var(--backdrop);
    font-family: "Open Sans", Arial, sans-serif;
  }
  .card-set {
    position: absolute;
    inset: 0;
    display: flex;
    align-items: center;
    justify-content: center;
    gap: 60px;
  }
  .business-card {
    width: 504px;
    height: 288px;
    border-radius: 3px;
    box-shadow: 0 2px 6px rgba(0,0,0,0.12);
    display: flex;
    flex-direction: column;
    align-items: center;
    justify-content: center;
    text-align: center;
  }
  .card-front { background: var(--card-white); }
  .card-back { background: var(--brand-teal); }

  .brand-lockup {
    display: flex;
    align-items: center;
    gap: 14px;
  }
  .brand-dot {
    width: 44px;
    height: 44px;
    border-radius: 50%;
    background: var(--logo-teal);
  }
  .brand-name {
    font-weight: 300;
    font-size: 38px;
    color: var(--logo-teal);
    letter-spacing: 0.5px;
  }

  .contact-dot {
    width: 30px;
    height: 30px;
    border-radius: 50%;
    background: var(--ink-light);
    margin-bottom: 12px;
  }
  .person-name {
    font-weight: 700;
    font-size: 17px;
    color: var(--ink-dark);
  }
  .person-role {
    font-weight: 400;
    font-size: 14px;
    color: var(--ink-light);
    margin-top: 2px;
  }
  .divider {
    width: 160px;
    height: 1px;
    margin: 10px 0 12px;
    background: linear-gradient(90deg, rgba(255,255,255,0), rgba(255,255,255,0.9), rgba(255,255,255,0));
  }
  .address {
    font-style: normal;
    font-size: 15px;
    line-height: 1.3;
    color: var(--ink-dark);
  }
</style>
</head>
<body>
  <main class="card-set">
    <section class="business-card card-front" aria-label="Card front">
      <div class="brand-lockup">
        <span class="brand-dot"></span>
        <span class="brand-name">Openbreath Harmony</span>
      </div>
    </section>

    <section class="business-card card-back" aria-label="Card back">
      <span class="contact-dot"></span>
      <h1 class="person-name">Maren Tollefsen</h1>
      <p class="person-role">Director</p>
      <div class="divider"></div>
      <address class="address">
        42 Quillfern Avenue<br>
        Dunmorrow, VIC 3806<br>
        ph 0451 628 904
      </address>
    </section>
  </main>
</body>
</html>
```